Counselling/ Wellness Clinic Needing Business Card & Matching Brochure

Looking for a brochure and business card that matches our brand, see logo and screen shots of our rebranding webpage.
We would like a QR code that takes to our website. The rebranding website that is not active will be lanternbrookcalming.ca
You we see we like depth, feeling through colours which has been through gradient. We want the brochure to show our services and make us stand out. The final design should match the website in a creative way.

```html
<!DOCTYPE html>
<html lang="en">
<head>
<meta charset="utf-8">
<title>Lanternbrook Calming Center – Brochure</title>
<link rel="stylesheet" href="https://fonts.googleapis.com/css2?family=Montserrat:wght@400;500;600;700;800&family=Pacifico&display=swap">
<style>
:root{
  --backdrop:#d9d9db;
  --ink:#1f1d2b;
  --text:#3b3a4a;
  --lavender:#ecdff4;
  --lilac:#c58be0;
  --violet:#8f5ad6;
  --indigo:#5b5fd6;
  --sky:#a9d6e8;
  --aqua:#3fb7d6;
  --mist:#e9f1f6;
  --brand:#6a64d8;
}
*{margin:0;padding:0;box-sizing:border-box}
html,body{width:1200px;height:2700px;overflow:hidden;background:var(--backdrop)}
body{position:relative;font-family:"Montserrat",sans-serif;color:var(--text)}
.page{position:absolute;width:560px;height:792px;overflow:hidden;box-shadow:0 10px 30px rgba(40,30,70,.18)}
.page > svg.bg{position:absolute;inset:0;width:100%;height:100%}

/* front cover */
.front-cover{background:linear-gradient(205deg,var(--lilac) 0%,#b9a3e7 38%,var(--sky) 72%,#d3e8f1 100%)}
.brand-name{position:absolute;font-family:"Montserrat",sans-serif;font-weight:600;color:var(--brand);display:flex;align-items:center;gap:8px;white-space:nowrap}
.brand-name .dot{width:14px;height:14px;border-radius:50%;background:var(--brand)}
.front-cover .brand-name{right:34px;top:84px;font-size:17px}
.cover-photo{position:absolute;left:118px;top:150px;width:330px;height:330px;border-radius:50%;
  background:radial-gradient(circle at 55% 45%,#ffffff 0%,#e7dcf4 35%,#b79be0 70%,#8d6fcf 100%)}
.cover-headline{position:absolute;left:0;right:0;top:500px;text-align:center;font-family:"Pacifico",cursive;font-size:40px;line-height:1.15;color:var(--ink)}
.cover-intro{position:absolute;left:58px;right:58px;top:618px;text-align:center;font-size:13px;line-height:1.5;color:var(--ink)}
.url-pill{position:absolute;left:50%;transform:translateX(-50%);top:708px;padding:6px 22px;border-radius:20px;
  background:linear-gradient(90deg,var(--aqua),var(--violet));color:#fff;font-size:12px;font-weight:500}

/* back cover */
.back-cover{background:linear-gradient(180deg,#a7d4e6 0%,#a9c6e6 45%,#bba6e8 80%,#d4a9ea 100%)}
.contact-list{position:absolute;left:44px;top:590px;list-style:none}
.contact-list li{display:flex;align-items:flex-start;gap:10px;font-size:12px;color:var(--ink);margin-bottom:10px;line-height:1.35}
.contact-list .icon{flex:none;width:18px;height:18px;border-radius:50%;background:linear-gradient(135deg,var(--aqua),var(--violet));display:flex;align-items:center;justify-content:center}
.contact-list .icon svg{width:10px;height:10px}

/* inner spread */
.inner-left{background:linear-gradient(180deg,#eef3f8 0%,#e4eef6 60%,#eadff5 100%)}
.inner-right{background:linear-gradient(180deg,#f3ecf8 0%,#ece3f6 60%,#e8e6f6 100%)}
.spread-photo{position:absolute;left:380px;top:1824px;width:360px;height:250px;border-radius:50%;clip-path:inset(0 0 0 0 round 0);
  background:linear-gradient(135deg,#6d5b55 0%,#b9a49a 35%,#e9e4e2 60%,#8a8fa6 100%)}
.inner-left .brand-name{left:34px;top:56px;font-size:13px}
.section-title{position:absolute;font-weight:800;letter-spacing:1px;background:linear-gradient(90deg,var(--aqua),var(--indigo));-webkit-background-clip:text;background-clip:text;color:transparent}
.services-title{left:44px;top:220px;font-size:30px}
.service{position:absolute;left:44px;width:470px;display:flex;gap:14px}
.service .badge{flex:none;width:38px;height:38px;border-radius:50%;background:linear-gradient(135deg,var(--aqua),var(--indigo));display:flex;align-items:center;justify-content:center}
.service .badge svg{width:22px;height:22px}
.service h3{font-size:11.5px;font-weight:700;color:var(--ink);margin-bottom:3px}
.service p{font-size:10px;line-height:1.45}
.about-title{left:44px;top:250px;font-size:28px}
.about-block{position:absolute;left:44px;width:470px}
.pill-heading{display:inline-block;padding:3px 14px;border-radius:14px;background:linear-gradient(90deg,var(--aqua),var(--indigo));color:#fff;font-size:13px;font-weight:700;margin-bottom:6px}
.about-block p{font-size:10px;line-height:1.45;margin-bottom:6px}
.about-photo{position:absolute;right:40px;top:292px;width:120px;height:120px;border-radius:50%;border:3px solid #c9b8ee;
  background:linear-gradient(135deg,#5f6c86 0%,#c4b1a8 45%,#eae4e0 70%,#7f7387 100%)}
.about-who p{width:300px}
</style>
</head>
<body>

<!-- Front cover on its own -->
<section class="page front-cover" style="left:320px;top:80px">
  <svg class="bg" viewBox="0 0 560 792" preserveAspectRatio="none" aria-hidden="true">
    <path d="M0 0 H560 V240 C420 180 260 60 0 40 Z" fill="var(--lavender)" opacity=".92"/>
    <path d="M0 470 C160 430 360 470 560 560 V792 H0 Z" fill="#ffffff" opacity=".22"/>
    <path d="M0 560 C200 520 380 580 560 660 V792 H0 Z" fill="#ffffff" opacity=".2"/>
  </svg>
  <div class="brand-name"><span class="dot"></span>Lanternbrook Calming Center</div>
  <div class="cover-photo" role="img" aria-label="Photo of a butterfly resting on lavender flowers"></div>
  <h1 class="cover-headline">Your healing journey<br>begins here</h1>
  <p class="cover-intro">Embrace your journey through transformation. We guide you through your personal journey, helping you transform and find completeness, just like a butterfly emerging and puzzle pieces coming together.</p>
  <div class="url-pill">lanternbrookcalming.ca</div>
</section>

<!-- Outer spread: back cover + front cover -->
<section class="page back-cover" style="left:40px;top:952px">
  <svg class="bg" viewBox="0 0 560 792" preserveAspectRatio="none" aria-hidden="true">
    <path d="M0 0 H560 V70 C380 20 180 30 0 90 Z" fill="var(--lavender)" opacity=".85"/>
    <path d="M0 540 C200 500 380 540 560 620 V792 H0 Z" fill="#ffffff" opacity=".2"/>
  </svg>
  <ul class="contact-list">
    <li><span class="icon"><svg viewBox="0 0 10 10"><path d="M2 1l2 2-1 1c.5 1.2 1.3 2 2.5 2.5l1-1 2 2-1.2 1.2C4.5 8.5 1.5 5.5 1 2.2Z" fill="#fff"/></svg></span>555-014-2290</li>
    <li><span class="icon"><svg viewBox="0 0 10 10"><rect x="1" y="2.5" width="8" height="5.5" rx=".8" fill="none" stroke="#fff"/><path d="M1.3 3l3.7 2.7L8.7 3" fill="none" stroke="#fff"/></svg></span>hello@lanternbrookcalming.ca</li>
    <li><span class="icon"><svg viewBox="0 0 10 10"><path d="M5 9.5S2 6 2 4a3 3 0 016 0c0 2-3 5.5-3 5.5Z" fill="#fff"/><circle cx="5" cy="4" r="1" fill="#8f5ad6"/></svg></span>48 Willowmere Road, Suite 3,<br>Brookfield, ON K0A 1B2</li>
    <li><span class="icon"><svg viewBox="0 0 10 10"><circle cx="5" cy="5" r="3.8" fill="none" stroke="#fff"/><path d="M1.2 5h7.6M5 1.2c-2 2.2-2 5.4 0 7.6M5 1.2c2 2.2 2 5.4 0 7.6" fill="none" stroke="#fff" stroke-width=".8"/></svg></span>www.lanternbrookcalming.ca</li>
  </ul>
</section>

<section class="page front-cover" style="left:600px;top:952px">
  <svg class="bg" viewBox="0 0 560 792" preserveAspectRatio="none" aria-hidden="true">
    <path d="M0 0 H560 V240 C420 180 260 60 0 40 Z" fill="var(--lavender)" opacity=".92"/>
    <path d="M0 470 C160 430 360 470 560 560 V792 H0 Z" fill="#ffffff" opacity=".22"/>
    <path d="M0 560 C200 520 380 580 560 660 V792 H0 Z" fill="#ffffff" opacity=".2"/>
  </svg>
  <div class="brand-name"><span class="dot"></span>Lanternbrook Calming Center</div>
  <div class="cover-photo" role="img" aria-label="Photo of a butterfly resting on lavender flowers"></div>
  <h1 class="cover-headline">Your healing journey<br>begins here</h1>
  <p class="cover-intro">Embrace your journey through transformation. We guide you through your personal journey, helping you transform and find completeness, just like a butterfly emerging and puzzle pieces coming together.</p>
  <div class="url-pill">lanternbrookcalming.ca</div>
</section>

<!-- Inner spread: services + about -->
<section class="page inner-left" style="left:40px;top:1824px">
  <svg class="bg" viewBox="0 0 560 792" preserveAspectRatio="none" aria-hidden="true">
    <defs><linearGradient id="waveLeft" x1="0" x2="1"><stop offset="0" stop-color="#c77be0"/><stop offset="1" stop-color="#b7c6ef"/></linearGradient></defs>
    <path d="M0 640 C160 600 340 640 560 700 V792 H0 Z" fill="url(#waveLeft)" opacity=".75"/>
  </svg>
  <div class="brand-name"><span class="dot"></span>Lanternbrook Calming Center</div>
  <h2 class="section-title services-title">OUR SERVICES</h2>
  <div class="service" style="top:280px">
    <span class="badge"><svg viewBox="0 0 22 22"><circle cx="11" cy="8" r="3.5" fill="none" stroke="#fff" stroke-width="1.5"/><path d="M4.5 18c1-4 12-4 13 0" fill="none" stroke="#fff" stroke-width="1.5"/></svg></span>
    <div><h3>INDIVIDUAL COUNSELLING</h3><p>We offer one-on-one sessions with a registered therapist who listens closely, helps you untangle what weighs on you and builds coping skills for a wide range of everyday challenges.</p></div>
  </div>
  <div class="service" style="top:362px">
    <span class="badge"><svg viewBox="0 0 22 22"><circle cx="7.5" cy="8" r="2.8" fill="none" stroke="#fff" stroke-width="1.4"/><circle cx="14.5" cy="8" r="2.8" fill="none" stroke="#fff" stroke-width="1.4"/><path d="M2.5 17c.8-3.5 9.2-3.5 10 0M9.5 17c.8-3.5 9.2-3.5 10 0" fill="none" stroke="#fff" stroke-width="1.4"/></svg></span>
    <div><h3>COUPLES COUNSELLING</h3><p>Are you and your partner struggling in your relationship? Our couples sessions help you rebuild trust, improve communication and find healthier ways through conflict, for every kind of partnership.</p></div>
  </div>
  <div class="service" style="top:444px">
    <span class="badge"><svg viewBox="0 0 22 22"><circle cx="8" cy="7" r="3" fill="none" stroke="#fff" stroke-width="1.4"/><circle cx="15" cy="10" r="2.2" fill="none" stroke="#fff" stroke-width="1.4"/><path d="M2.5 17c.8-3.8 10.2-3.8 11 0M12 17c.6-2.8 6.4-2.8 7 0" fill="none" stroke="#fff" stroke-width="1.4"/></svg></span>
    <div><h3>CHILD &amp; YOUTH COUNSELLING</h3><p>Looking for support for your child? Growing up can be hard. Our therapists use play, talk and creative tools to help young people ages six and up feel heard and understood.</p></div>
  </div>
  <div class="service" style="top:526px">
    <span class="badge"><svg viewBox="0 0 22 22"><circle cx="6" cy="8" r="2.4" fill="none" stroke="#fff" stroke-width="1.3"/><circle cx="16" cy="8" r="2.4" fill="none" stroke="#fff" stroke-width="1.3"/><circle cx="11" cy="11.5" r="1.9" fill="none" stroke="#fff" stroke-width="1.3"/><path d="M2 17c.6-3 7.4-3 8 0M12 17c.6-3 7.4-3 8 0" fill="none" stroke="#fff" stroke-width="1.3"/></svg></span>
    <div><h3>FAMILY COUNSELLING</h3><p>Is your family going through a difficult time? Family sessions open space for every voice, ease tension at home and help each member feel closer, calmer and better supported.</p></div>
  </div>
</section>

<section class="page inner-right" style="left:600px;top:1824px">
  <svg class="bg" viewBox="0 0 560 792" preserveAspectRatio="none" aria-hidden="true">
    <defs><linearGradient id="waveRight" x1="0" x2="1"><stop offset="0" stop-color="#b7c6ef"/><stop offset=".6" stop-color="#c77be0"/><stop offset="1" stop-color="#3fb7d6"/></linearGradient></defs>
    <path d="M0 700 C200 660 400 690 560 650 V792 H0 Z" fill="url(#waveRight)" opacity=".8"/>
  </svg>
  <h2 class="section-title about-title">ABOUT US</h2>
  <div class="about-photo" role="img" aria-label="Photo of a counselling session in a bright office"></div>
  <div class="about-block about-who" style="top:292px">
    <span class="pill-heading">Who We Are</span>
    <p>We are an eclectic team of registered therapists with years of experience and a shared belief that healing happens in a warm, safe space where you are truly heard.</p>
    <p>We know that life can feel like a long road at times. Our work is to walk beside you, one gentle step after another, until the path feels clear again.</p>
  </div>
  <div class="about-block" style="top:470px">
    <span class="pill-heading">What We Do</span>
    <p>We offer individual, couples, child and youth, and family counselling, both in person and online, in several languages, for people facing anxiety, grief, trauma, stress and change.</p>
  </div>
  <div class="about-block" style="top:560px">
    <span class="pill-heading">Why Work With Us</span>
    <p>Our therapists work within a caring, team-based approach. We meet you where you are, respect your pace and tailor every plan so you leave each session feeling lighter and better equipped.</p>
  </div>
</section>

<div class="spread-photo" role="img" aria-label="Photo of therapists talking with clients in a counselling room"></div>

</body>
</html>
```